Weightloss company needs Business Card

We want a business card that is clean and professional, yet portrays that we are a friendly, innovative, and versatile program designed to fit the needs of our clients.
I would like there to be 2 sides, one side having an appointment card, and the other side containing the logo and business information. There can be decorations on both sides. The logo is attached.

Target Market(s)

Men and women 40-60

Industry/Entity Type

Business

Contact Information for Business Card

Font styles to use
Sans Serif

Requirements
Must have
• The logo, space for business information
Nice to have
• The colors in the logo
Should not have
• No pictures of people or food

```html
<!DOCTYPE html>
<html lang="en">
<head>
<meta charset="utf-8">
<title>Brightpath Wellness – Business Card</title>
<link rel="stylesheet" href="https://fonts.googleapis.com/css2?family=Open+Sans:wght@400;600;700&display=swap">
<style>
  :root {
    --brand-red: #ff0a3a;
    --card-top: #eeeeee;
    --paper: #ffffff;
    --backdrop: #e4e2df;
    --ink-light: #ffffff;
  }
  * { margin: 0; padding: 0; box-sizing: border-box; }
  html, body { width: 1200px; height: 900px; overflow: hidden; }
  body {
    background: var(--backdrop);
    font-family: "Open Sans", Arial, sans-serif;
    position: relative;
  }
  .card {
    position: absolute;
    display: flex;
    flex-direction: column;
    box-shadow: 0 6px 18px rgba(0,0,0,0.12);
  }
  .card-front { left: 238px; top: 62px; width: 555px; height: 343px; }
  .card-back { left: 457px; top: 518px; width: 560px; height: 344px; }

  .logo-area {
    background: var(--card-top);
    display: flex;
    align-items: center;
    justify-content: center;
    gap: 14px;
  }
  .card-front .logo-area { height: 185px; }
  .card-back .logo-area { height: 187px; }
  .brand-mark {
    width: 22px; height: 22px; border-radius: 50%;
    background: var(--brand-red);
  }
  .brand-name {
    color: var(--brand-red);
    font-weight: 700;
    font-size: 34px;
    letter-spacing: 0.3px;
  }

  .info-band {
    flex: 1;
    background: var(--brand-red);
    color: var(--ink-light);
    position: relative;
  }
  .person { position: absolute; right: 291px; top: 36px; text-align: right; }
  .person-name { font-size: 20px; font-weight: 600; line-height: 1.2; }
  .person-role { font-size: 14px; line-height: 1.5; }
  .contacts { position: absolute; left: 288px; top: 28px; list-style: none; }
  .contacts li {
    display: flex; align-items: center; gap: 9px;
    font-size: 14.5px; line-height: 20px;
  }
  .contacts svg { width: 12px; height: 12px; fill: var(--ink-light); }
  .address { position: absolute; left: 104px; top: 106px; font-size: 14.5px; }

  .appointment {
    flex: 1;
    background: var(--paper);
    color: var(--brand-red);
    text-align: center;
    padding-top: 8px;
  }
  .appointment-title { font-size: 22px; font-weight: 600; margin-bottom: 14px; }
  .field { font-size: 14px; font-weight: 700; margin-bottom: 18px; letter-spacing: 0.2px; }
  .dots { font-weight: 400; letter-spacing: 0.5px; }
  .notice { font-size: 14.5px; }
</style>
</head>
<body>
  <section class="card card-front">
    <div class="logo-area">
      <span class="brand-mark"></span>
      <span class="brand-name">Brightpath Wellness</span>
    </div>
    <div class="info-band">
      <div class="person">
        <p class="person-name">Daniel Harper</p>
        <p class="person-role">Managing Director</p>
      </div>
      <ul class="contacts">
        <li><svg viewBox="0 0 24 24"><path d="M6.6 10.8a15.2 15.2 0 0 0 6.6 6.6l2.2-2.2c.3-.3.7-.4 1-.2 1.1.4 2.3.6 3.6.6.6 0 1 .4 1 1V20c0 .6-.4 1-1 1A17 17 0 0 1 3 4c0-.6.4-1 1-1h3.5c.6 0 1 .4 1 1 0 1.3.2 2.5.6 3.6.1.3 0 .7-.2 1z"/></svg>021-555 010 246</li>
        <li><svg viewBox="0 0 24 24"><path d="M2 5h20v14H2z M2 5l10 7 10-7" stroke="#ff0a3a" stroke-width="1.5"/></svg>hello@brightpathwell.com</li>
        <li><svg viewBox="0 0 24 24"><circle cx="12" cy="12" r="10"/><path d="M2 12h20M12 2c3 3 3 17 0 20M12 2c-3 3-3 17 0 20" stroke="#ff0a3a" stroke-width="1.5" fill="none"/></svg>www.brightpathwell.com</li>
      </ul>
      <p class="address">48 Linden Avenue, Maple Grove, Northland, 204815.</p>
    </div>
  </section>

  <section class="card card-back">
    <div class="logo-area">
      <span class="brand-mark"></span>
      <span class="brand-name">Brightpath Wellness</span>
    </div>
    <div class="appointment">
      <h2 class="appointment-title">Your Next Appointment is</h2>
      <p class="field">Name: <span class="dots">.............................................................................</span></p>
      <p class="field">Date: <span class="dots">..........................................</span>Time:<span class="dots">...........................</span></p>
      <p class="notice">If unable to keep appointment,&nbsp; kindly give 24hrs notice.</p>
    </div>
  </section>
</body>
</html>
```